Business Card Design

We need a new business card design for our company, Lumen Forge.

Our website: www.brightrow7.ca

We are open to all ideas, from professional to very creative.
Updates

Design update requests:

1. We would like to see some examples with "BrightRow7" instead of "Lumen Forge" as the company name.
2. Would like to see "Software | Web | Branding" included on the card somewhere as well.

Thanks.

We are really trying to express the nature of our business through our business card.  "Lumen" can be misconstrued for the health industry, so use of "BrightRow7" and the "Software | Web | Branding" slogan are key to understanding our business.

We have uploaded a new PSD which includes a monitor, tablet, and phone screen.  This represents the flexibility of web applications and is another tool we would like to see used on business cards.

We will be eliminating designs today and will await updated designs with these new specs.

Thank-you.

Industry/Entity Type

Business

Requirements
Must have
• Content:
First M. Last
Managing Partner
e. email@brightrow7.ca
p. 555.555.5555

```html
<!DOCTYPE html>
<html lang="en">
<head>
<meta charset="utf-8">
<title>Lumen Forge — Business Card</title>
<link rel="stylesheet" href="https://fonts.googleapis.com/css2?family=Michroma&family=Gochi+Hand&display=swap">
<style>
  :root {
    --page: #ffffff;
    --bleed: #cccccc;
    --frame-line: #333333;
    --card-front: #ffffff;
    --card-back: #e4e4e4;
    --divider: #cfcfcf;
    --brand-grey: #58595b;
    --brand-blue: #1aa3dd;
    --ink: #1a1a1a;
    --dot: #666666;
    --dash: #8a8a8a;
  }
  html, body {
    margin: 0;
    padding: 0;
    width: 1200px;
    height: 1023px;
    overflow: hidden;
    background: var(--page);
  }
  .sheet {
    position: relative;
    width: 1200px;
    height: 1023px;
  }
  .bleed-frame {
    position: absolute;
    left: 186px;
    width: 818px;
    height: 363px;
    background: var(--bleed);
    border: 1px solid var(--frame-line);
    box-sizing: border-box;
  }
  .bleed-frame--front { top: 89px; }
  .bleed-frame--back { top: 525px; }

  .card {
    position: absolute;
    left: 53px;
    top: 33px;
    width: 710px;
    height: 291px;
  }
  .card--front {
    background: var(--card-front);
    display: flex;
    align-items: center;
    justify-content: center;
    gap: 22px;
  }
  .brand-square {
    width: 44px;
    height: 44px;
    background: var(--brand-blue);
  }
  .brand-name {
    font-family: "Michroma", sans-serif;
    font-size: 34px;
    letter-spacing: 1px;
    color: var(--brand-grey);
    margin: 0;
    text-transform: uppercase;
  }

  .card--back {
    background: var(--card-back);
  }
  .card-divider {
    position: absolute;
    left: 288px;
    top: 0;
    width: 2px;
    height: 100%;
    background: var(--divider);
  }
  .contact {
    position: absolute;
    left: 65px;
    top: 61px;
    margin: 0;
    padding: 0;
    list-style: none;
    font-family: "Gochi Hand", cursive;
    font-size: 21px;
    line-height: 32.5px;
    color: var(--ink);
  }
  .contact .phone { font-size: 24px; }

  .note-lines {
    position: absolute;
    left: 317px;
    top: 70px;
  }
</style>
</head>
<body>
<main class="sheet">
  <section class="bleed-frame bleed-frame--front" aria-label="Card front">
    <div class="card card--front">
      <span class="brand-square" aria-hidden="true"></span>
      <h1 class="brand-name">Lumen Forge</h1>
    </div>
  </section>

  <section class="bleed-frame bleed-frame--back" aria-label="Card back">
    <div class="card card--back">
      <ul class="contact">
        <li class="name">First M. Last</li>
        <li class="title">Managing Partner</li>
        <li class="email">e. email@brightrow7.ca</li>
        <li class="phone">p. 555.555.5555</li>
      </ul>
      <div class="card-divider"></div>
      <svg class="note-lines" width="360" height="170" viewBox="0 0 360 170" aria-hidden="true">
        <g stroke="#8a8a8a" stroke-width="1.2" stroke-dasharray="6 4">
          <line x1="8" y1="8" x2="347" y2="8"/>
          <line x1="8" y1="47" x2="347" y2="47"/>
          <line x1="8" y1="87" x2="347" y2="87"/>
          <line x1="8" y1="126" x2="347" y2="126"/>
          <line x1="8" y1="166" x2="347" y2="166"/>
        </g>
        <g fill="#666666">
          <circle cx="8" cy="8" r="7.5"/><circle cx="347" cy="8" r="7.5"/>
          <circle cx="8" cy="47" r="7.5"/><circle cx="347" cy="47" r="7.5"/>
          <circle cx="8" cy="87" r="7.5"/><circle cx="347" cy="87" r="7.5"/>
          <circle cx="8" cy="126" r="7.5"/><circle cx="347" cy="126" r="7.5"/>
          <circle cx="8" cy="161" r="7.5"/><circle cx="347" cy="161" r="7.5"/>
        </g>
      </svg>
    </div>
  </section>
</main>
</body>
</html>
```